Harbor Crest Engineers (HarborCE)
Project: Business cards
Business cards - Information Technology
Business cards
Professional
Dana R. Kessler, CISSP
Principal Systems Engineer
P.O. Box 8073 Crestview MD 20799
dkessler@harbor-crest-eng.example
www.harbor-crest-eng.example

```html
<!DOCTYPE html>
<html lang="en">
<head>
<meta charset="utf-8">
<title>Harbor Crest Engineers — Business Cards</title>
<link rel="stylesheet" href="https://fonts.googleapis.com/css2?family=Open+Sans:wght@400;600;700;800&display=swap">
<style>
  :root {
    --stage: #3a3b3d;
    --blue-light: #2fa3e6;
    --blue: #1478c8;
    --blue-deep: #0b4f94;
    --orange: #f07a1a;
    --white: #ffffff;
    --ink-blue: #0e62b0;
    --muted: #4a6f94;
  }
  * { box-sizing: border-box; margin: 0; padding: 0; }
  html, body {
    width: 1200px; height: 904px; overflow: hidden;
    background: var(--stage);
    font-family: "Open Sans", Arial, sans-serif;
  }
  .sheet {
    position: relative; width: 1200px; height: 904px;
    display: flex; flex-direction: column; align-items: center;
    justify-content: center; gap: 44px;
  }
  .card {
    width: 700px; height: 400px; position: relative; overflow: hidden;
    border-radius: 4px;
  }

  /* Front */
  .card-front {
    background: radial-gradient(ellipse at 50% 45%, var(--blue-light) 0%, var(--blue) 45%, var(--blue-deep) 100%);
    display: flex; align-items: center; justify-content: center;
  }
  .front-mark {
    display: flex; align-items: center; gap: 16px;
    color: var(--white); font-weight: 700; font-size: 46px; letter-spacing: 1px;
  }
  .front-mark .dot {
    width: 54px; height: 54px; border-radius: 50%; background: var(--white);
  }

  /* Back */
  .card-back { background: var(--white); }
  .back-brand {
    position: absolute; left: 0; right: 0; top: 44px;
    display: flex; flex-direction: column; align-items: center;
  }
  .brand-row { display: flex; align-items: center; gap: 12px; }
  .brand-row .dot {
    width: 30px; height: 30px; border-radius: 50%; background: var(--orange);
  }
  .brand-name {
    color: var(--ink-blue); font-weight: 800; font-size: 30px; letter-spacing: 1px;
    text-transform: uppercase;
  }
  .brand-tagline {
    margin-top: 4px; color: var(--muted); font-size: 11px; font-weight: 600;
    letter-spacing: 3.4px; text-transform: uppercase;
  }
  .name-band {
    position: absolute; left: 0; right: 0; top: 150px; height: 40px;
    display: flex; align-items: stretch;
  }
  .name-band .holder {
    width: 52%; background: var(--orange); color: var(--white);
    display: flex; align-items: center; justify-content: flex-end;
    padding-right: 14px; font-size: 17px; font-weight: 600;
  }
  .name-band .title {
    flex: 1; display: flex; align-items: center; padding-left: 14px;
    color: var(--orange); font-size: 16px; font-weight: 600;
    border-left: 3px solid var(--white);
  }
  .contact-panel {
    position: absolute; left: 0; right: 0; top: 190px; bottom: 0;
    background: linear-gradient(160deg, var(--blue-light) 0%, var(--blue) 55%, var(--blue-deep) 100%);
    display: flex; padding: 30px 0 0;
  }
  .address {
    width: 52%; padding-right: 18px; text-align: right;
    color: var(--white); font-size: 15px; line-height: 24px; padding-top: 34px;
  }
  .contact-list {
    list-style: none; padding-left: 18px; color: var(--white);
    font-size: 14px; line-height: 30px;
  }
  .contact-list li { display: flex; align-items: center; gap: 10px; }
  .contact-list svg { width: 16px; height: 16px; flex: none; }
</style>
</head>
<body>
<main class="sheet">
  <section class="card card-front" aria-label="Card front">
    <div class="front-mark"><span class="dot"></span><span>HarborCE</span></div>
  </section>

  <section class="card card-back" aria-label="Card back">
    <div class="back-brand">
      <div class="brand-row"><span class="dot"></span><span class="brand-name">Harbor Crest Engineers</span></div>
      <div class="brand-tagline">Building Dependable IT Networks</div>
    </div>

    <div class="name-band">
      <div class="holder">Dana R. Kessler, CISSP</div>
      <div class="title">Principal Systems Engineer</div>
    </div>

    <div class="contact-panel">
      <div class="address">P.O. Box 8073<br>Crestview MD 20799</div>
      <ul class="contact-list">
        <li>
          <svg viewBox="0 0 16 16"><rect x="4" y="1" width="8" height="14" rx="1.5" fill="none" stroke="#fff" stroke-width="1.5"/><circle cx="8" cy="12.5" r="0.9" fill="#fff"/></svg>
          301-555-0142
        </li>
        <li>
          <svg viewBox="0 0 16 16"><path d="M4 2l2.5 3-1.5 1.5a8 8 0 004.5 4.5L11 9.5l3 2.5-1.5 2C7 14 2 9 2 3.5z" fill="#fff"/></svg>
          301-555-0187
        </li>
        <li>
          <svg viewBox="0 0 16 16"><rect x="1.5" y="3.5" width="13" height="9" rx="1" fill="none" stroke="#fff" stroke-width="1.5"/><path d="M2 4l6 5 6-5" fill="none" stroke="#fff" stroke-width="1.5"/></svg>
          dkessler@harbor-crest-eng.example
        </li>
        <li>
          <svg viewBox="0 0 16 16"><circle cx="8" cy="8" r="6.3" fill="none" stroke="#fff" stroke-width="1.4"/><ellipse cx="8" cy="8" rx="2.8" ry="6.3" fill="none" stroke="#fff" stroke-width="1.2"/><path d="M1.8 8h12.4" stroke="#fff" stroke-width="1.2"/></svg>
          www.harbor-crest-eng.example
        </li>
      </ul>
    </div>
  </section>
</main>
</body>
</html>
```